Career Drop Down Layout on CopperTrailhead.com Quiz Results

We want to redesign the career drop down view after people take the career finder quiz at CopperTrailhead.com. After you take the quiz (feel free to take it yourself), you get a results page. On the left hand navigation bar, go to Career Matches (in green). When you open one of your career matches, we want people to see lots of great information about the job. We need help figuring out how to display the information. The information we want to display is the following:

1) name of job
2) JOBLEX description
3) Link to the Joblex info
4) Match dial
5) Rising Demand image
6) a video about the job
7) Average salary
8) Minimum Qualifications
9) Top Tips
10) Recommended Programs
11) Jobs in their area - by Hire Lantern

I put screen shots of what we have now and a mock-up of the new elements in the brief. It can look anyway you think will be good. I'm not tied to the mock-up at all.

To see how your design will look live on the web do the following:

1) Login at: https://www.coppertrailhead.com/survey/login (or take the quiz yourself to see your own results)
2) Enter Email address: dana.kowal@copperventure.org
3) Enter Password: 123456
4) See results summary - Click on Career Matches from the left navigation bar
5) See the career matches, when you click the arrow on the right side of each career match it will display the new page you are designing for each career with info from a database.

Thanks, Dana

Target Market(s)

Young people looking for jobs

Number of Pages Required

1 page

Requirements
Must have
• The layout of how all the information will look nicely on a computer screen. It can scroll down more vertically if necessary.

The color scheme and text must match the existing site since this page will be embedded in our site. I attached our design guide.
Nice to have
• I'd like to see a very easy to scan, organized way to display a lot of job information.

```html
<!DOCTYPE html>
<html lang="en">
<head>
<meta charset="utf-8">
<title>Career Matches – CopperTrailhead</title>
<link rel="stylesheet" href="https://fonts.googleapis.com/css2?family=Cabin:wght@400;500;600&family=Raleway:wght@400;500;600&family=Lato:wght@400;700&display=swap">
<style>
:root{
  --indigo:#5b3fa6;
  --indigo-dark:#4a2f94;
  --green:#4caf2f;
  --green-bright:#6cc33b;
  --green-nav:#3f8a3a;
  --panel-bg:#e6ece4;
  --panel-head:#e6e4f2;
  --text:#222;
  --body:#333;
  --orange:#f5a300;
  --pink:#e85fb0;
}
*{box-sizing:border-box;margin:0;padding:0}
html,body{width:1200px;height:975px;overflow:hidden;background:#fff;font-family:"Lato",sans-serif;color:var(--text)}
body{position:relative}
.site-header{position:absolute;left:0;top:0;width:1200px;height:68px;background:#fff;border-bottom:1px solid #dcd8ec}
.brand{position:absolute;left:23px;top:24px;display:flex;align-items:center;gap:7px;font-family:"Cabin",sans-serif;font-weight:600;font-size:19px;color:var(--green)}
.brand-dot{width:11px;height:11px;border-radius:50%;background:var(--green)}
.top-nav{position:absolute;top:28px;font-size:12.5px;color:#333;letter-spacing:.2px}
.logout{position:absolute;left:1061px;top:15px;width:86px;height:39px;border-radius:20px;background:var(--indigo-dark);color:#fff;font-size:12.5px;font-weight:700;display:flex;align-items:center;justify-content:center}
.sidebar{position:absolute;left:0;top:68px;width:252px;height:907px;background:var(--indigo)}
.sidebar h2{font-family:"Cabin",sans-serif;font-weight:600;color:#fff;font-size:21px;text-align:center;padding-top:37px;height:98px}
.side-menu{list-style:none;border-top:1px solid #8d7cc4}
.side-menu li{height:31.6px;border-bottom:1px solid #8d7cc4;color:#fff;font-size:14px;display:flex;align-items:center;justify-content:center}
.side-menu li.active{background:var(--green-nav);font-weight:700}
.pdf-btn{position:absolute;left:43px;top:362px;width:162px;height:31px;border-radius:16px;background:var(--green-bright);color:#fff;font-size:15.5px;display:flex;align-items:center;justify-content:center;box-shadow:0 2px 3px rgba(0,0,0,.25)}
.page-title{position:absolute;left:588px;top:112px;display:flex;align-items:center;gap:8px;font-family:"Cabin",sans-serif;font-size:30px;font-weight:500;color:#111}
.intro{position:absolute;left:252px;width:936px;text-align:center;font-size:13.5px;color:#222}
.matches-box{position:absolute;left:299px;top:263px;width:840px;height:712px;border:1px solid #222;border-bottom:none}
.fav-title{position:absolute;left:632px;top:289px;display:flex;align-items:center;gap:10px;font-family:"Cabin",sans-serif;font-size:23px;font-weight:600}
.career-head{position:absolute;left:316px;top:378px;width:804px;height:45px;background:var(--panel-head);display:flex;align-items:center;padding-left:40px;gap:7px}
.career-head .name{font-family:"Cabin",sans-serif;font-size:19px;margin-left:12px;color:#111}
.career-head .caret{position:absolute;right:42px;top:18px;width:0;height:0;border-left:9px solid transparent;border-right:9px solid transparent;border-bottom:9px solid #333}
.career-body{position:absolute;left:316px;top:423px;width:804px;height:504px;background:var(--panel-bg);font-family:"Raleway",sans-serif}
.career-body > *{position:absolute}
.h-industry{left:26px;top:20px;font-size:19px;font-weight:500;color:var(--indigo)}
.h-sub{left:26px;font-size:16px;font-weight:500;color:var(--indigo)}
.desc{left:26px;top:160px;width:404px;font-size:12px;line-height:19.3px;color:var(--body);text-align:justify}
.desc-pos{top:160px}
.joblex-btn{left:26px;top:240px;display:flex;align-items:center;height:33px;padding:0 14px;border-radius:17px;background:var(--indigo-dark);color:#fff;font-size:12px;font-weight:600}
.tips{left:26px;top:333px;width:404px;list-style:none}
.tips li{font-size:12px;line-height:19.3px;color:var(--body);text-align:justify;margin-bottom:5px}
.min-qual{left:26px;top:423px;font-size:17px;font-weight:500;color:var(--indigo)}
.salary-label{left:474px;top:22px;width:121px;text-align:center;font-size:13px;font-weight:500;color:var(--indigo)}
.salary-pill{left:474px;top:45px;width:121px;height:32px;border-radius:16px;background:var(--green);color:#fff;font-family:"Cabin",sans-serif;font-weight:600;font-size:25px;display:flex;align-items:center;justify-content:center}
.outlook{left:474px;top:99px;display:flex;align-items:center;gap:3px;font-weight:600;font-size:16px;color:var(--orange)}
.gauge{left:634px;top:19px}
.match-level{left:620px;top:100px;width:176px;text-align:center;font-size:13.5px;color:#222}
.video{left:474px;top:141px;width:307px;height:173px;background:linear-gradient(115deg,#e24fb2 0%,#d44aa8 45%,#1d7a7c 60%,#0e6166 100%);overflow:hidden}
.video .play{position:absolute;left:132px;top:66px;width:42px;height:42px;border-radius:50%;background:rgba(255,255,255,.92)}
.video .play::after{content:"";position:absolute;left:16px;top:12px;border-left:15px solid #333;border-top:9px solid transparent;border-bottom:9px solid transparent}
.programs-title{left:474px;top:338px;font-size:16px;font-weight:500;color:var(--indigo)}
.program{left:474px;display:flex;align-items:center;font-size:12.5px;color:var(--body)}
.arrow{width:17px;height:17px;border-radius:50%;background:var(--pink);margin-right:10px;position:relative;flex:none}
.arrow::after{content:"";position:absolute;left:6px;top:4px;border-left:6px solid #fff;border-top:4.5px solid transparent;border-bottom:4.5px solid transparent}
.badge{left:736px;width:22px;height:22px;background:#dfe7f2;border:1px solid #9bb0cc}
.jobs-title{left:474px;top:440px;font-size:16px;font-weight:500;color:var(--indigo)}
.jobs-link{left:474px;top:470px;display:flex;align-items:center;font-size:12.5px;color:var(--body)}
.jobs-link b{font-weight:600;color:var(--indigo-dark);margin-left:4px}
</style>
</head>
<body>
<header class="site-header">
  <div class="brand"><span class="brand-dot"></span>Copper Trailhead</div>
  <nav>
    <span class="top-nav" style="left:810px">HOME</span>
    <span class="top-nav" style="left:871px">MY RESULTS ˅</span>
    <span class="top-nav" style="left:973px">SERVICES ˅</span>
  </nav>
  <div class="logout">LOG OUT</div>
</header>

<aside class="sidebar">
  <h2>Dana's Results</h2>
  <ul class="side-menu">
    <li>Results Summary</li>
    <li>What Motivates You</li>
    <li>Your DISC Profile</li>
    <li class="active">Career Matches</li>
    <li>Maximize My Results</li>
    <li>Communication Tips</li>
    <li>Reflections and Goals</li>
    <li>Resources</li>
  </ul>
  <div class="pdf-btn">Download PDF</div>
</aside>

<h1 class="page-title">
  <svg width="48" height="48" viewBox="0 0 48 48" aria-hidden="true"><circle cx="24" cy="24" r="24" fill="#6cc33b"/><circle cx="18" cy="21" r="5" fill="#fff"/><path d="M9 38c1-8 5-11 9-11s8 3 9 11z" fill="#fff"/><rect x="30" y="10" width="3" height="26" fill="#4a2f94"/><rect x="27" y="12" width="12" height="5" fill="#fff"/><rect x="25" y="19" width="12" height="5" fill="#fff"/></svg>
  Career Matches
</h1>
<p class="intro" style="top:188px">Rate as many jobs as you can,
  <svg width="26" height="26" viewBox="0 0 26 26" style="vertical-align:middle"><circle cx="13" cy="13" r="12" fill="#4caf2f"/><circle cx="13" cy="13" r="8.5" fill="#fff"/></svg> = send to favorites,
  <svg width="26" height="26" viewBox="0 0 26 26" style="vertical-align:middle"><circle cx="13" cy="13" r="12" fill="#777"/><circle cx="13" cy="13" r="8.5" fill="#fff"/></svg> = Not sure,
  <svg width="26" height="26" viewBox="0 0 26 26" style="vertical-align:middle"><circle cx="13" cy="13" r="12" fill="#d63a3a"/><circle cx="13" cy="13" r="8.5" fill="#fff"/></svg> = No way - send to archive!</p>
<p class="intro" style="top:213px">Click on each category for in-depth descriptions, resources, education options, and tips.</p>

<section class="matches-box"></section>
<div class="fav-title">
  <svg width="72" height="72" viewBox="0 0 72 72" aria-hidden="true"><circle cx="36" cy="36" r="34" fill="#4caf2f" stroke="#222" stroke-width="2"/><circle cx="36" cy="36" r="27" fill="#fff"/><path d="M24 34h8v20h-8zM34 34l6-12c3 0 5 2 4 6l-1 5h9c3 0 4 3 3 5l-3 13c-1 2-2 3-4 3H34z" fill="#fff" stroke="#222" stroke-width="2.5" stroke-linejoin="round"/></svg>
  Favorites
</div>

<div class="career-head">
  <svg width="30" height="30" viewBox="0 0 30 30"><circle cx="15" cy="15" r="13.5" fill="#4caf2f" stroke="#222" stroke-width="1"/><circle cx="15" cy="15" r="9.5" fill="#fff"/><path d="M10 14h3v8h-3zM14 14l3-5c1 0 2 1 2 3l-1 2h4c1 0 2 1 1 2l-1 5c0 1-1 1-2 1h-6z" fill="#fff" stroke="#222" stroke-width="1.2"/></svg>
  <svg width="30" height="30" viewBox="0 0 30 30"><circle cx="15" cy="15" r="13.5" fill="#bbb"/><circle cx="15" cy="15" r="9.5" fill="#ddd"/></svg>
  <svg width="30" height="30" viewBox="0 0 30 30"><circle cx="15" cy="15" r="13.5" fill="#ef9a9a"/><circle cx="15" cy="15" r="9.5" fill="#f6c7c7"/></svg>
  <span class="name">Life Coaching</span>
  <span class="caret"></span>
</div>

<section class="career-body">
  <h3 class="h-industry">Industry: Holistic Development</h3>
  <h4 class="h-sub" style="top:56px">JOBLEX job description:</h4>
  <p class="desc" style="top:90px">Counsel individuals to maximize the independence and employability of persons coping with personal, social, and vocational difficulties that result from birth defects, illness, disease, accidents, aging, or the stress of daily life. Coordinate activities for residents of care and treatment facilities. Assess client needs and design and implement rehabilitation programs that may include personal and vocational counseling, training, and job placement.</p>
  <span class="joblex-btn">Learn more about this job on JOBLEX</span>
  <h4 class="h-sub" style="top:295px">Top TIPS:</h4>
  <ol class="tips">
    <li>1. You don’t need any formal training to become a life coach, but we recommend it.</li>
    <li>2. Life coaching relies on your personal brand so an authentic website is critical for attracting clients. Sitebloom is a great place to start.</li>
  </ol>
  <p class="min-qual">Minimum Qualification: NONE</p>

  <p class="salary-label">Average Salary</p>
  <div class="salary-pill">$50,900</div>
  <div class="outlook">Rising<svg width="20" height="20" viewBox="0 0 20 20"><circle cx="10" cy="10" r="6" fill="#f5c400" stroke="#f5a300" stroke-width="2"/></svg>Demand</div>

  <svg class="gauge" width="148" height="68" viewBox="0 0 148 68" role="img" aria-label="Match level dial">
    <g fill="none" stroke-width="22">
      <path d="M16 66 A58 58 0 0 1 24 37" stroke="#d42a2a"/>
      <path d="M24 37 A58 58 0 0 1 45 16" stroke="#f08a1c"/>
      <path d="M45 16 A58 58 0 0 1 74 8" stroke="#f2c424"/>
      <path d="M74 8 A58 58 0 0 1 103 16" stroke="#9bcc3a"/>
      <path d="M103 16 A58 58 0 0 1 124 37" stroke="#4caf2f"/>
      <path d="M124 37 A58 58 0 0 1 132 66" stroke="#5b3fa6"/>
    </g>
    <path d="M6 66 A68 68 0 0 1 142 66" fill="none" stroke="#bbb" stroke-width="9"/>
    <g font-family="Raleway,sans-serif" font-size="6" font-weight="600" fill="#222">
      <text x="62" y="9">GOOD</text>
      <text x="30" y="22" transform="rotate(-40 30 22)">FAIR</text>
      <text x="12" y="50" transform="rotate(-75 12 50)">LOW</text>
      <text x="104" y="12" transform="rotate(35 104 12)">GREAT</text>
      <text x="130" y="24" transform="rotate(68 130 24)">EXCELLENT</text>
    </g>
    <circle cx="74" cy="66" r="15" fill="#fff"/>
    <path d="M74 62 L120 55 L75 70 Z" fill="#222"/>
    <circle cx="74" cy="66" r="6" fill="#222"/>
  </svg>
  <p class="match-level">Your match level (12)</p>

  <div class="video" role="img" aria-label="Video thumbnail: a life coach talks about earning six figures without certification">
    <span class="play"></span>
  </div>

  <p class="programs-title">Preferred Online Programs:</p>
  <div class="program" style="top:369px"><span class="arrow"></span>Mentor Craft Academy</div>
  <span class="badge" style="top:365px"></span>
  <div class="program" style="top:402px"><span class="arrow"></span>Global Guide Alliance</div>
  <span class="badge" style="top:398px"></span>

  <p class="jobs-title">Jobs in Your Area:</p>
  <div class="jobs-link"><span class="arrow"></span>See local openings<b>by Hire Lantern</b></div>
</section>
</body>
</html>
```